Qualvine.com needs a Mobile FIRST Site

Qualvine.com is an insurance broker based in Panama City, Panama that plans to sell car and motorcycle insurance online.

We need to design a total of 5 pages (two of those are A/B test pages). The site will be responsive and will be programmed in React. We will be using Bolt Kit´s library to code Qualvine.com. Keep in mind that we are using Bolt Kit to program the site´s functions, not to create the "look and feel" of the site, that is obviously your job. You can learn more about Bolt Kit here... https://boltkit.example/

We have created wireframes for the app. Please follow and keep in mind the instructions in the wireframes. You can change things here and there as long as the core functions and goals stay intact. We have uploaded the wireframes along with the company logo and color.

We are planning to A/B test the site´s home page so we need to design two homepages. You can find homepage A and B in the wireframes provided.

We speak Spanish in Panama but you can design the site in English. We can change the text once we receive the designs.

Target Market(s)

25-45 year olds who own a car or motorcylcle and own a credit card.

Industry/Entity Type

Insurance

Font styles to use
Sans Serif

Requirements
Must have
• Follow the wireframes provided and the logo colors.
Nice to have
• Please look at the Image I´ve uploaded from DeskHarbor, use it as reference to create HomePage A.

```html
<!DOCTYPE html>
<html lang="en">
<head>
<meta charset="utf-8">
<title>Qualvine.com – Home A / Home B</title>
<link rel="stylesheet" href="https://fonts.googleapis.com/css2?family=Lato:ital,wght@0,300;0,400;0,700;0,900;1,400&display=swap">
<style>
  :root{
    --night:#10102e;
    --night-light:#1e1c52;
    --brand:#3d2990;
    --brand-dark:#2a1c74;
    --brand-ink:#35258a;
    --paper:#efeef0;
    --card:#ffffff;
    --green:#5ea61f;
    --grey:#9a9a9a;
    --grey-line:#d9d9d9;
    --text:#3b3b3b;
    --muted:#5a5a5a;
    --gold:#f2c20f;
  }
  *{box-sizing:border-box;margin:0;padding:0}
  html,body{width:1200px;height:1200px;overflow:hidden;background:var(--night)}
  body{font-family:"Lato",sans-serif;position:relative}
  .backdrop{position:absolute;inset:0}
  .brand-mark{position:absolute;left:0;width:1200px;top:72px;text-align:center;color:#fff;font-weight:900;font-size:56px;letter-spacing:-1px}
  .screen-title{position:absolute;top:232px;width:360px;text-align:center;color:#fff;font-weight:400;font-size:29px;letter-spacing:1px}
  .thanks{position:absolute;left:505px;top:1044px;width:200px;height:56px;border-radius:8px;background:#3633a0}

  .phone{position:absolute;top:314px;width:360px;height:639px;background:var(--paper);overflow:hidden}
  .phone--a{left:178px}
  .phone--b{left:663px}
  .status-bar{position:absolute;left:0;top:0;width:100%;height:23px;background:var(--brand-dark);color:#fff;font-size:14px}
  .status-bar svg{position:absolute;right:60px;top:5px}
  .status-bar .clock{position:absolute;right:9px;top:3px}
  .app-bar{position:absolute;left:0;top:23px;width:100%;height:53px;background:var(--brand)}
  .menu-icon{position:absolute;left:22px;top:20px}
  .app-name{position:absolute;left:0;width:100%;top:14px;text-align:center;color:#fff;font-weight:900;font-size:21px}

  .claim-title{position:absolute;top:91px;width:100%;text-align:center;color:var(--brand-ink);font-weight:700;font-size:24px}
  .claim-lead{position:absolute;top:124px;width:100%;text-align:center;color:var(--muted);font-style:italic;font-size:12px;line-height:17px}

  .stepper{position:absolute;left:0;top:170px;width:100%;height:28px}
  .step-dot{position:absolute;top:1px;width:26px;height:26px;border-radius:50%;text-align:center;line-height:24px;font-size:12px}
  .step-dot.done{left:24px;border:1.5px solid var(--green)}
  .step-dot.current{left:157px;background:var(--green);color:#fff;line-height:26px}
  .step-dot.todo{left:285px;border:1.5px solid #c4c4c4;color:var(--grey)}
  .step-label{position:absolute;top:6px;font-size:12px}
  .step-label.done{left:55px;color:var(--green)}
  .step-label.current{left:188px;color:#333}
  .step-label.todo{left:316px;color:var(--grey)}
  .step-line{position:absolute;top:14px;height:1px}
  .step-line.done{left:102px;width:48px;background:var(--green)}
  .step-line.todo{left:226px;width:52px;background:#c4c4c4}

  .toggle{position:absolute;left:22px;top:214px;width:315px;height:36px;border:1px solid #c9c9c9;border-radius:3px;display:flex;overflow:hidden}
  .toggle-option{flex:1;display:flex;align-items:center;justify-content:center;gap:7px;font-size:15px;color:var(--grey)}
  .toggle-option.active{background:var(--brand);color:#fff}

  .plan-card{position:absolute;top:275px;width:149px;height:343px;background:var(--card);border-radius:3px}
  .plan-card.first{left:21px}
  .plan-card.second{left:186px}
  .ribbon{position:absolute;right:0;top:0}
  .photo{position:absolute;border-radius:4px}
  .plan-card .photo{left:8px;top:22px;width:133px;height:62px}
  .price{position:absolute;color:var(--brand-ink);font-size:16px;font-weight:400;text-align:center}
  .plan-card .price{left:0;width:100%;top:99px}
  .divider{position:absolute;left:0;width:100%;height:1px;background:#ececec}

  .cover-row{position:absolute;font-size:10px;color:var(--text)}
  .cover-row .amount{position:absolute;right:0;top:0}
  .cover-row .track{position:absolute;left:0;right:0;top:13px;height:2px;background:#e3e3e3}
  .cover-row .track i{position:absolute;left:0;top:0;height:2px;background:var(--brand);width:var(--fill)}
  .plan-card .cover-row{left:9px;width:133px;height:16px}

  .benefits{position:absolute;font-size:7px;color:var(--text);line-height:13px}
  .benefits h4{color:var(--brand-ink);font-size:10px;font-weight:700;margin-bottom:3px}
  .plan-card .benefits{left:8px;top:239px}
  .buy{position:absolute;height:28px;background:var(--brand);color:#fff;font-size:11px;text-align:center;line-height:26px;border-radius:2px;border-bottom:2px solid var(--brand-dark)}
  .plan-card .buy{left:18px;width:112px;top:306px}

  .tab{position:absolute;top:218px;height:36px;display:flex;align-items:center;justify-content:center;gap:6px;font-size:14px;border:1px solid #e0e0e0;border-bottom:none;border-radius:2px 2px 0 0}
  .tab.active{left:43px;width:133px;background:#fff;color:var(--brand-ink);font-weight:700}
  .tab.idle{left:183px;width:133px;background:#e6e6e6;color:var(--grey);top:221px;height:33px}
  .offer-list{position:absolute;left:22px;top:254px;width:314px;height:385px;background:#fff}
  .offer{position:absolute;left:0;width:100%;height:186px}
  .offer .photo{left:19px;top:12px;width:102px;height:88px}
  .offer .star{position:absolute;left:154px;top:6px}
  .offer .price{left:0;width:140px;top:103px}
  .offer .buy{left:15px;width:134px;top:129px;height:31px;font-size:12px;line-height:29px}
  .offer .cover-row{left:168px;width:133px;height:16px}
  .offer .benefits{left:167px;top:108px}
  .more{position:absolute;left:151px;top:362px}
</style>
</head>
<body>
  <svg class="backdrop" width="1200" height="1200" viewBox="0 0 1200 1200" aria-hidden="true">
    <rect width="1200" height="1200" fill="var(--night)"/>
    <polygon points="1200,24 1200,1200 40,1200" fill="var(--night-light)"/>
  </svg>

  <div class="brand-mark">Qualvine.com</div>
  <div class="screen-title" style="left:177px">HOME A</div>
  <div class="screen-title" style="left:662px">HOME B</div>

  <!-- Home A -->
  <section class="phone phone--a">
    <div class="status-bar">
      <svg width="52" height="14" viewBox="0 0 52 14"><path d="M0 2 Q9 -2 18 2 L9 13Z" fill="#fff"/><path d="M22 13 L34 1 V13Z" fill="#fff"/><rect x="42" y="1" width="8" height="13" rx="1" fill="#fff"/></svg>
      <span class="clock">12:30</span>
    </div>
    <header class="app-bar">
      <svg class="menu-icon" width="18" height="13" viewBox="0 0 18 13"><rect width="18" height="2" fill="#fff"/><rect y="5.5" width="18" height="2" fill="#fff"/><rect y="11" width="18" height="2" fill="#fff"/></svg>
      <div class="app-name">Qualvine.com</div>
    </header>
    <h1 class="claim-title">CLAIM HERE</h1>
    <p class="claim-lead">Lorem ipsum dolor sit amet consectetur adipiscing ullamd<br>orper ramolestie pharetra eros tiorper ncidunt amet.</p>
    <div class="stepper">
      <span class="step-dot done"><svg width="13" height="10" viewBox="0 0 13 10" style="margin-top:7px"><path d="M1 5 L5 9 L12 1" stroke="var(--green)" stroke-width="2" fill="none"/></svg></span>
      <span class="step-label done">Choose</span><span class="step-line done"></span>
      <span class="step-dot current">2</span><span class="step-label current">Verify</span><span class="step-line todo"></span>
      <span class="step-dot todo">3</span><span class="step-label todo">Pay</span>
    </div>
    <div class="toggle">
      <div class="toggle-option active"><svg width="38" height="14" viewBox="0 0 38 14"><path d="M1 11 V8 Q1 6 5 5 L11 4 Q16 0 24 1 L31 5 Q37 6 37 9 V11Z" fill="#fff"/><circle cx="9" cy="11" r="3" fill="var(--brand)" stroke="#fff" stroke-width="1.5"/><circle cx="29" cy="11" r="3" fill="var(--brand)" stroke="#fff" stroke-width="1.5"/></svg>Cars</div>
      <div class="toggle-option"><svg width="32" height="16" viewBox="0 0 32 16" fill="none" stroke="#b4b4b4" stroke-width="1.6"><circle cx="7" cy="10" r="5"/><circle cx="25" cy="10" r="5"/><path d="M7 10 L13 4 H20 L25 10 M13 4 L10 1"/></svg>Motorcycles</div>
    </div>

    <article class="plan-card first">
      <svg class="ribbon" width="38" height="38" viewBox="0 0 38 38"><polygon points="0,0 38,0 38,38" fill="var(--gold)"/><path d="M26 6 l2 4 4 .5-3 3 .8 4-3.8-2-3.8 2 .8-4-3-3 4-.5Z" fill="#fff"/></svg>
      <div class="photo" role="img" aria-label="Silver sedan photo" style="background:linear-gradient(180deg,#e9e9ec,#a7a9ae)"></div>
      <div class="price">$ 100.00</div>
      <div class="divider" style="top:128px"></div>
      <div class="cover-row" style="top:142px;--fill:66%">Vandalism<span class="amount">$ 10,000</span><span class="track"><i></i></span></div>
      <div class="cover-row" style="top:173px;--fill:87%">Fire<span class="amount">$ 20,000</span><span class="track"><i></i></span></div>
      <div class="cover-row" style="top:206px;--fill:78%">Explosion<span class="amount">$ 15,000</span><span class="track"><i></i></span></div>
      <div class="divider" style="top:233px"></div>
      <div class="benefits"><h4>Benefits</h4>– Praesent bero a massa sagittis<br>– Susp endisse consequ magna sed<br>– Nullam molestie massa blandit</div>
      <div class="buy">Buy Now</div>
    </article>

    <article class="plan-card second">
      <div class="photo" role="img" aria-label="Red hatchback photo" style="background:linear-gradient(180deg,#f2dede,#c8262c)"></div>
      <div class="price">$ 150.00</div>
      <div class="divider" style="top:128px"></div>
      <div class="cover-row" style="top:142px;--fill:70%">Vandalism<span class="amount">$ 10,000</span><span class="track"><i></i></span></div>
      <div class="cover-row" style="top:173px;--fill:87%">Fire<span class="amount">$ 20,000</span><span class="track"><i></i></span></div>
      <div class="cover-row" style="top:206px;--fill:82%">Explosion<span class="amount">$ 15,000</span><span class="track"><i></i></span></div>
      <div class="divider" style="top:233px"></div>
      <div class="benefits"><h4>Benefits</h4>– Praesent bero a massa sagittis<br>– Susp endisse consequ magna sed<br>– Nullam molestie massa blandit</div>
      <div class="buy">Buy Now</div>
    </article>
  </section>

  <!-- Home B -->
  <section class="phone phone--b">
    <div class="status-bar">
      <svg width="52" height="14" viewBox="0 0 52 14"><path d="M0 2 Q9 -2 18 2 L9 13Z" fill="#fff"/><path d="M22 13 L34 1 V13Z" fill="#fff"/><rect x="42" y="1" width="8" height="13" rx="1" fill="#fff"/></svg>
      <span class="clock">12:30</span>
    </div>
    <header class="app-bar">
      <svg class="menu-icon" width="18" height="13" viewBox="0 0 18 13"><rect width="18" height="2" fill="#fff"/><rect y="5.5" width="18" height="2" fill="#fff"/><rect y="11" width="18" height="2" fill="#fff"/></svg>
      <div class="app-name">Qualvine.com</div>
    </header>
    <h1 class="claim-title">CLAIM HERE</h1>
    <p class="claim-lead">Lorem ipsum dolor sit amet consectetur adipiscing ullamd<br>orper ramolestie pharetra eros tiorper ncidunt amet.</p>
    <div class="stepper">
      <span class="step-dot done"><svg width="13" height="10" viewBox="0 0 13 10" style="margin-top:7px"><path d="M1 5 L5 9 L12 1" stroke="var(--green)" stroke-width="2" fill="none"/></svg></span>
      <span class="step-label done">Choose</span><span class="step-line done"></span>
      <span class="step-dot current">2</span><span class="step-label current">Verify</span><span class="step-line todo"></span>
      <span class="step-dot todo">3</span><span class="step-label todo">Pay</span>
    </div>

    <div class="tab active"><svg width="28" height="15" viewBox="0 0 32 16" fill="none" stroke="var(--brand-ink)" stroke-width="1.8"><circle cx="7" cy="10" r="5"/><circle cx="25" cy="10" r="5"/><path d="M7 10 L13 4 H20 L25 10 M13 4 L10 1"/></svg>Motorcycles</div>
    <div class="tab idle"><svg width="38" height="14" viewBox="0 0 38 14"><path d="M1 11 V8 Q1 6 5 5 L11 4 Q16 0 24 1 L31 5 Q37 6 37 9 V11Z" fill="#9a9a9a"/><circle cx="9" cy="11" r="3" fill="#e6e6e6" stroke="#9a9a9a" stroke-width="1.5"/><circle cx="29" cy="11" r="3" fill="#e6e6e6" stroke="#9a9a9a" stroke-width="1.5"/></svg>Cars</div>

    <div class="offer-list">
      <article class="offer" style="top:0">
        <div class="photo" role="img" aria-label="Vintage olive motorcycle photo" style="background:linear-gradient(180deg,#eeeadb,#8f8a5a)"></div>
        <svg class="star" width="16" height="16" viewBox="0 0 16 16"><path d="M8 0 l2.4 5 5.6.7-4.1 3.8 1 5.5L8 12.3 3.1 15l1-5.5L0 5.7 5.6 5Z" fill="var(--gold)"/></svg>
        <div class="price">$ 100.00</div>
        <div class="buy">Buy Now</div>
        <div class="cover-row" style="top:16px;--fill:78%">Vandalism<span class="amount">$ 10,000</span><span class="track"><i></i></span></div>
        <div class="cover-row" style="top:47px;--fill:82%">Fire<span class="amount">$ 20,000</span><span class="track"><i></i></span></div>
        <div class="cover-row" style="top:80px;--fill:68%">Explosion<span class="amount">$ 15,000</span><span class="track"><i></i></span></div>
        <div class="benefits"><h4>Benefits</h4>– Praesent bero a massa sagittis<br>– Susp endisse consequ magna sed<br>– Nullam molestie massa blandit</div>
        <div class="divider" style="top:179px"></div>
      </article>
      <article class="offer" style="top:186px">
        <div class="photo" role="img" aria-label="Red scooter photo" style="background:linear-gradient(180deg,#f6e4df,#e0412c)"></div>
        <div class="price">$ 100.00</div>
        <div class="buy">Buy Now</div>
        <div class="cover-row" style="top:16px;--fill:74%">Vandalism<span class="amount">$ 10,000</span><span class="track"><i></i></span></div>
        <div class="cover-row" style="top:47px;--fill:82%">Fire<span class="amount">$ 20,000</span><span class="track"><i></i></span></div>
        <div class="cover-row" style="top:80px;--fill:68%">Explosion<span class="amount">$ 15,000</span><span class="track"><i></i></span></div>
        <div class="benefits"><h4>Benefits</h4>– Praesent bero a massa sagittis<br>– Susp endisse consequ magna sed<br>– Nullam molestie massa blandit</div>
      </article>
      <svg class="more" width="12" height="12" viewBox="0 0 12 12" fill="none" stroke="#777" stroke-width="1.2"><path d="M1 2 L6 6 L11 2 M1 6 L6 10 L11 6"/></svg>
    </div>
  </section>

  <div class="thanks" role="img" aria-label="Hand-lettered thank you message"></div>
</body>
</html>
```